Reed & Vale NC grand opening (for BILLBOARD)

Advertising the grand opening of our cannabis/hemp shop in NC. We will sell all things hemp (flower, cartridges, disposables, edibles, creams, lotions, pet products etc...)

Requirements
Must have
• include, open starting Aug 1, but grand opening Aug 15th.
Nice to have
• Difference slogan ideas "Save some cash, buy our grass" "Find your perfect high at Reed & Vale cannabis store" "Experience Nature's Gift: Reed & Vale Cannabis Store"

```html
<!DOCTYPE html>
<html lang="en">
<head>
<meta charset="utf-8">
<title>Reed &amp; Vale – Billboard Options</title>
<link href="https://fonts.googleapis.com/css2?family=Montserrat:wght@500;700;800&display=swap" rel="stylesheet">
<style>
  :root {
    --stage: #484647;
    --title: #ffffff;
    --board-white: #ffffff;
    --board-mist: #e9ebea;
    --leaf-tint: #eef6ee;
    --green: #7cc242;
    --navy: #0f1238;
  }
  * { margin: 0; padding: 0; box-sizing: border-box; }
  html, body {
    width: 1200px; height: 1200px; overflow: hidden;
    background: var(--stage);
    font-family: "Montserrat", sans-serif;
  }
  .sheet { position: relative; width: 1200px; height: 1200px; }
  .sheet-title {
    position: absolute; top: 172px; left: 0; width: 1200px;
    text-align: center; color: var(--title);
    font-weight: 800; font-size: 52px; line-height: 60px; letter-spacing: 0.3px;
  }
  .billboard {
    position: absolute; width: 1058px; height: 312px;
    box-shadow: 10px 14px 22px rgba(0,0,0,0.55);
    overflow: hidden;
  }
  .billboard--pattern { top: 269px; left: 71px; background: var(--board-mist); }
  .billboard--plain { top: 700px; left: 68px; width: 1063px; height: 311px; background: var(--board-white); }
  .leaf-pattern {
    position: absolute; inset: 0;
    background:
      radial-gradient(ellipse 200px 150px at 14% 40%, var(--leaf-tint), transparent 70%),
      radial-gradient(ellipse 220px 160px at 88% 35%, var(--leaf-tint), transparent 70%),
      radial-gradient(ellipse 170px 120px at 60% 88%, var(--leaf-tint), transparent 70%),
      var(--board-mist);
  }
  .billboard-copy { position: absolute; inset: 0; text-align: center; }
  .slogan {
    position: absolute; top: 34px; left: 0; width: 100%;
    color: var(--green); font-weight: 700; font-size: 25px; line-height: 24px;
    padding-left: 62px;
  }
  .brand-name {
    position: absolute; top: 84px; left: 0; width: 100%;
    color: var(--green); font-weight: 500; font-size: 88px; line-height: 88px;
    letter-spacing: -1px;
  }
  .store-type {
    position: absolute; top: 177px; left: 0; width: 100%;
    color: var(--navy); font-weight: 800; font-size: 66px; line-height: 66px;
    letter-spacing: 0.5px; padding-right: 32px;
  }
  .directions {
    position: absolute; top: 252px; left: 0; width: 100%;
    color: var(--green); font-weight: 700; font-size: 28px; line-height: 28px;
    padding-left: 36px;
  }
  .opening-dates {
    position: absolute; top: 285px; left: 0; width: 100%;
    color: var(--navy); font-weight: 700; font-size: 18px; line-height: 20px;
    letter-spacing: 0.5px;
  }
</style>
</head>
<body>
  <main class="sheet">
    <h1 class="sheet-title">BILLBOARD OPTIONS</h1>

    <section class="billboard billboard--pattern">
      <div class="leaf-pattern" role="img" aria-label="Faint pale green pattern of large cannabis leaves across the background"></div>
      <div class="billboard-copy">
        <p class="slogan">Experience<br>Nature's Gift:</p>
        <p class="brand-name">Reed &amp; Vale</p>
        <p class="store-type">CANNABIS STORE</p>
        <p class="directions">EXIT 6A BIRCHFIELD RD</p>
        <p class="opening-dates">OPEN STARTING AUG 1 · GRAND OPENING AUG 15TH</p>
      </div>
    </section>

    <section class="billboard billboard--plain">
      <div class="billboard-copy">
        <p class="slogan">Experience<br>Nature's Gift:</p>
        <p class="brand-name">Reed &amp; Vale</p>
        <p class="store-type">CANNABIS STORE</p>
        <p class="directions">EXIT 6A BIRCHFIELD RD</p>
        <p class="opening-dates">OPEN STARTING AUG 1 · GRAND OPENING AUG 15TH</p>
      </div>
    </section>
  </main>
</body>
</html>
```